Natural Essential Oil Packaging

We would like you to develop a line of packaging for natural essential oil products from a company named “Lan Suoi Bich.”
List of items to be designed:
- 01 Company logo
- Air freshener (spray) product: 01 Package design + 01 label design
- 02 essential oil (glass containers) variants: 02 Label designs + 01 “how to use” attached instruction tag
Description:
A. Company logo:
- Company name: Lan Suoi Bich (“Tram” is the Vietnamese name for melaleuca);
- symbolizing "pure, natural, untouched, Lan Suoi Bich, essential,";
- should consist of text and graphic;
- should suggest a stylized drop of oil;
B. Air freshener (spray) product (Packaging and label design)
a. Product description
- Oil extracted from the unique Vietnamese cajeput trees
- Strength: pleasant aroma, air cleansing, virus and bacteria cleaning and prevention, insect expelling
- Used for: air refreshing, relaxing, spa-effect, air cleaning, air-born virus prevention (flu virus), insect expelling
- Application: air spray
b. Package to design: 170ml glass spray bottle
c. Label text for design: brand name: Vorenta + variant name “Lemongrass” + Air Freshener + Melaleuca Essential Oil
C. 02 essential oil (glass containers) variants (Label and Instrution Tag designs)
a. Production description:
i. 02 product variant under the brand name Tuscavi
1 - Vietnamese Cajeput Oil: Special breed of cajeput only found in Vietnam, known for amazingly pleasant fragrance giving senses of relaxation, refreshment, peace while at the same time, driving off potential disease carrying elements in the air
2 - Australian tea trea oil: Australian breed of malaleuca known for effective healing of skin from various types of infection, skin protection and highly effective oral hygiene
ii. Product values:
1. 100% pure oil, 100% organic, 100% environment and human friendly, NO chemical
2. aiming to promote human’s well being, health, nature sustainability, improve living environment
3. both products are about nurturing, uplifting, healing and recovering
4. both place their values on authenticity, originality, nature, exotic natural ingredients, green and organic life style
5. both have zero chemical and artificial substance hence 100% safe for long time and frequent usage
iii. SKU: 10ml glass container
iv. Application: for both topical and oral use
b. Label text for design:
i. brand name: Tuscavi + variant name: Cajeput Oil / Tea Tree Oil
D. Creative elements are suggested to be communicating organicity, understated premiumness, nature, lightness, nurturing
PLEASE SEE ATTACHED FILES FOR BETTER BRIEF DETAILS AND LAYOUTS.

```html
<!DOCTYPE html>
<html lang="en">
<head>
<meta charset="utf-8">
<title>Lan Suoi Bich – Essential Oil Packaging</title>
<link rel="stylesheet" href="https://fonts.googleapis.com/css2?family=Alegreya:wght@400;500&family=Tinos&display=swap">
<style>
  :root {
    --page: #ffffff;
    --cream: #f1e7cc;
    --ink: #4a3a22;
    --ornament-light: #e6d6b4;
    --ornament-dark: #c7ad86;
    --mark: #b58a68;
    --caption: #1a1a1a;
  }
  * { box-sizing: border-box; margin: 0; padding: 0; }
  html, body { width: 1200px; height: 900px; overflow: hidden; background: var(--page); }
  .sheet { position: relative; width: 1200px; height: 900px; font-family: "Alegreya", Georgia, serif; color: var(--ink); }

  .caption { position: absolute; font-family: "Tinos", "Times New Roman", serif; font-size: 11px; letter-spacing: .3px; color: var(--caption); text-align: center; width: 200px; }

  .label { position: absolute; background: var(--cream); }
  .label > * { position: absolute; left: 0; right: 0; text-align: center; line-height: 1; white-space: nowrap; }

  .brandmark { display: flex; justify-content: center; align-items: center; gap: 3px; font-size: 12px; letter-spacing: .5px; text-transform: uppercase; }
  .brandmark .dot { width: 9px; height: 9px; border-radius: 50%; background: var(--mark); flex: none; }

  .range-name { font-weight: 400; }
  .variant-name { font-weight: 500; }
  .fine-print { font-size: 6px; }
  .body-copy { white-space: normal; font-size: 7.6px; line-height: 12.4px; padding: 0 36px; }
  .body-copy p + p { margin-top: 12px; }

  .flourish-band { left: auto; right: auto; background: linear-gradient(90deg, rgba(199,173,134,0) 0%, var(--ornament-light) 12%, var(--ornament-dark) 50%, var(--ornament-light) 88%, rgba(199,173,134,0) 100%); opacity: .75; }

  .signature { position: absolute; left: 690px; top: 778px; width: 470px; height: 112px; display: flex; align-items: center; gap: 14px; }
  .signature .dot { width: 62px; height: 62px; border-radius: 50%; background: var(--mark); flex: none; }
  .signature .name { font-size: 50px; letter-spacing: 2px; text-transform: uppercase; color: #111; white-space: nowrap; }
</style>
</head>
<body>
<main class="sheet">

  <!-- Cajeut front / back -->
  <div class="caption" style="left:50px; top:36px;">(FRONT PACKAGING)</div>
  <div class="caption" style="left:338px; top:36px;">(BACK PACKAGING)</div>

  <section class="label" style="left:20px; top:58px; width:263px; height:358px;">
    <div class="brandmark" style="top:46px;"><span class="dot"></span>Lan Suoi Bich</div>
    <div class="range-name" style="top:64px; font-size:22px;">Tuscavi</div>
    <div class="variant-name" style="top:135px; font-size:26px;">Cajeput Oil</div>
    <div class="flourish-band" role="img" aria-label="Decorative swirl flourish band" style="left:30px; width:202px; top:160px; height:28px;"></div>
    <div class="fine-print" style="top:188px;">100% pure oil, 100% organic, 100% environment and human friendly</div>
    <div class="fine-print" style="top:196px;">10ml glass container</div>
  </section>

  <section class="label" style="left:300px; top:58px; width:263px; height:358px;">
    <div class="brandmark" style="top:20px;"><span class="dot"></span>Lan Suoi Bich</div>
    <div class="range-name" style="top:39px; font-size:22px;">Tuscavi</div>
    <div class="flourish-band" role="img" aria-label="Decorative swirl flourish band" style="left:30px; width:205px; top:94px; height:28px;"></div>
    <div class="body-copy" style="top:131px;">
      <p>100% pure oil, 100% organic, 100% environment and human friendly.<br>Topical and oral use.</p>
      <p>Vietnamese Cajeput Oil: Special breed of cajeput only found in Vietnam, known for amazingly pleasant fragrance giving senses of relaxation, refreshment, peace while at the same time, driving off potential disease carrying elements in the air.</p>
    </div>
    <div class="flourish-band" role="img" aria-label="Decorative swirl flourish band" style="left:30px; width:205px; top:232px; height:28px;"></div>
  </section>

  <!-- Tea tree front / back -->
  <div class="caption" style="left:56px; top:473px;">(FRONT PACKAGING)</div>
  <div class="caption" style="left:339px; top:473px;">(BACK PACKAGING)</div>

  <section class="label" style="left:24px; top:496px; width:265px; height:362px;">
    <div class="brandmark" style="top:44px;"><span class="dot"></span>Lan Suoi Bich</div>
    <div class="range-name" style="top:65px; font-size:22px;">Tuscavi</div>
    <div class="variant-name" style="top:136px; font-size:26px;">Tea Tree Oil</div>
    <div class="flourish-band" role="img" aria-label="Decorative swirl flourish band" style="left:30px; width:205px; top:160px; height:28px;"></div>
    <div class="fine-print" style="top:189px;">100% pure oil, 100% organic, 100% environment and human friendly</div>
    <div class="fine-print" style="top:197px;">10ml glass container</div>
  </section>

  <section class="label" style="left:307px; top:496px; width:265px; height:362px;">
    <div class="brandmark" style="top:19px;"><span class="dot"></span>Lan Suoi Bich</div>
    <div class="range-name" style="top:39px; font-size:22px;">Tuscavi</div>
    <div class="flourish-band" role="img" aria-label="Decorative swirl flourish band" style="left:30px; width:205px; top:96px; height:28px;"></div>
    <div class="body-copy" style="top:132px;">
      <p>100% pure oil, 100% organic, 100% environment and human friendly.<br>Topical and oral use.</p>
      <p>Australian tea trea oil: Australian breed of malaleuca known for effective healing of skin from various types of infection, skin protection and highly effective oral hygiene.</p>
    </div>
    <div class="flourish-band" role="img" aria-label="Decorative swirl flourish band" style="left:30px; width:205px; top:226px; height:28px;"></div>
  </section>

  <!-- Air freshener -->
  <section class="label" style="left:694px; top:36px; width:439px; height:230px;">
    <div class="brandmark" style="top:30px; font-size:10px;"><span class="dot" style="width:7px;height:7px;"></span>Lan Suoi Bich</div>
    <div class="range-name" style="top:46px; font-size:18px;">Vorenta</div>
    <div class="variant-name" style="top:94px; font-size:27px;">Lemongrass</div>
    <div style="top:150px; font-size:9px;">Melaleuca Essential Oil Air Freshener</div>
    <div class="fine-print" style="top:164px;">170ml</div>
  </section>

  <!-- Bottle labels -->
  <section class="label" style="left:766px; top:287px; width:295px; height:229px;">
    <div class="brandmark" style="top:26px; font-size:22px; gap:5px;"><span class="dot" style="width:16px;height:16px;"></span>Lan Suoi Bich</div>
    <div class="range-name" style="top:53px; font-size:34px;">Tuscavi</div>
    <div class="variant-name" style="top:95px; font-size:48px;">Cajeput Oil</div>
    <div class="flourish-band" role="img" aria-label="Decorative swirl flourish band" style="left:32px; width:224px; top:141px; height:58px;"></div>
    <div style="top:198px; font-size:10.5px;">100% pure oil, 100% organic, 100% environment and human friendly</div>
    <div style="top:211px; font-size:10.5px;">10ml</div>
  </section>

  <section class="label" style="left:766px; top:535px; width:295px; height:226px;">
    <div class="brandmark" style="top:20px; font-size:22px; gap:5px;"><span class="dot" style="width:16px;height:16px;"></span>Lan Suoi Bich</div>
    <div class="range-name" style="top:46px; font-size:34px;">Tuscavi</div>
    <div class="variant-name" style="top:88px; font-size:48px;">Tea Tree Oil</div>
    <div class="flourish-band" role="img" aria-label="Decorative swirl flourish band" style="left:32px; width:224px; top:141px; height:57px;"></div>
    <div style="top:196px; font-size:10.5px;">100% pure oil, 100% organic, 100% environment and human friendly</div>
    <div style="top:209px; font-size:10.5px;">10ml</div>
  </section>

  <!-- Brand signature -->
  <div class="signature">
    <span class="dot"></span>
    <span class="name">Lan Suoi Bich</span>
  </div>

</main>
</body>
</html>
```